2 Business Card Designs

Need two business cards designed:
1) for lumora studio (wedding video) website is lumorastudio.com.au
2) for lumora studio (corporate video) website is lumorastudio.net.au

I am looking for something simple, no fancy shapes etc. Just elegant, simple and classy.

Both companies are video companies, one specialising in weddings the other corporate videos. Neither card needs to have any pics of video or camera related images. Please use same colour schemes as respective websites.

Logo is the same but can change colour.

Industry/Entity Type

Camera

Requirements
Must have
• Logo should be either all white or a colour to match websites
Should not have
• swirls, flowers, shapes, etc.

```html
<!DOCTYPE html>
<html lang="en">
<head>
<meta charset="utf-8">
<title>Lumora Studio – Business Card</title>
<link href="https://fonts.googleapis.com/css2?family=Josefin+Sans:wght@300;400&display=swap" rel="stylesheet">
<style>
  :root {
    --page-bg: #ffffff;
    --card-dark: #1f1f1f;
    --card-back: #262626;
    --card-mid: #3a3f45;
    --card-sheen: #5d7180;
    --ink-light: #ffffff;
    --ink-soft: #e6e9ec;
    --card-shadow: rgba(0, 0, 0, 0.25);
  }
  * { box-sizing: border-box; margin: 0; padding: 0; }
  html, body {
    width: 1200px;
    height: 800px;
    overflow: hidden;
    background: var(--page-bg);
    font-family: "Josefin Sans", sans-serif;
  }
  .canvas { position: relative; width: 1200px; height: 800px; }

  .card {
    position: absolute;
    width: 545px;
    height: 334px;
    border-radius: 23px;
    overflow: hidden;
    box-shadow: 0 2px 6px var(--card-shadow);
    color: var(--ink-light);
  }

  /* Front */
  .card-front {
    left: 32px;
    top: 192px;
    background: linear-gradient(120deg, var(--card-dark) 0%, var(--card-mid) 30%, var(--card-sheen) 48%, var(--card-mid) 64%, var(--card-dark) 100%);
  }
  .brand-name {
    position: absolute;
    right: 22px;
    top: 6px;
    text-align: right;
    font-weight: 300;
    color: var(--ink-light);
    line-height: 1;
  }
  .brand-name .word-main { display: block; font-size: 60px; letter-spacing: 1px; }
  .brand-name .word-sub { display: block; font-size: 20px; letter-spacing: 11px; margin-top: -2px; margin-right: -11px; }

  .person {
    position: absolute;
    left: 18px;
    top: 148px;
  }
  .person-name { font-size: 35px; font-weight: 300; line-height: 1; }
  .person-role { font-size: 20px; font-weight: 300; margin-top: 4px; }

  .contact-list {
    position: absolute;
    left: 285px;
    top: 155px;
    list-style: none;
    font-size: 12.5px;
    font-weight: 300;
    color: var(--ink-soft);
  }
  .contact-list li { display: flex; align-items: center; height: 18px; }
  .contact-list svg { width: 11px; height: 11px; margin-right: 5px; flex: none; }

  .web-band {
    position: absolute;
    left: 0;
    right: 0;
    bottom: 0;
    height: 65px;
    background: var(--card-dark);
    border-top: 2px solid var(--ink-light);
    padding-left: 16px;
    display: flex;
    align-items: center;
    font-size: 37px;
    font-weight: 300;
    letter-spacing: 0.5px;
  }

  /* Back: diagonal oversized wordmark bleeding off the card */
  .card-back {
    left: 623px;
    top: 280px;
    background: var(--card-back);
  }
  .back-mark .word-main,
  .back-mark .word-sub {
    position: absolute;
    display: block;
    white-space: nowrap;
    font-weight: 300;
    color: var(--ink-light);
    transform: rotate(-28deg);
  }
  .back-mark .word-main {
    left: 14px;
    top: 150px;
    font-size: 180px;
    line-height: 180px;
    letter-spacing: 2px;
    transform-origin: 0 142px;
  }
  .back-mark .word-sub {
    left: 128px;
    top: 293px;
    font-size: 42px;
    line-height: 42px;
    letter-spacing: 42px;
    transform-origin: 0 33px;
  }
</style>
</head>
<body>
<main class="canvas">

  <section class="card card-front" aria-label="Business card front">
    <div class="brand-name">
      <span class="word-main">lumora</span>
      <span class="word-sub">STUDIO</span>
    </div>

    <div class="person">
      <p class="person-name">Daniel Hartley</p>
      <p class="person-role">Owner/Director</p>
    </div>

    <ul class="contact-list">
      <li>
        <svg viewBox="0 0 12 12" aria-hidden="true"><rect width="12" height="12" rx="2" fill="#fff"/><path d="M3.4 2.6l1.3-.2.7 1.8-.9.7c.5 1 1.2 1.7 2.2 2.2l.7-.9 1.8.7-.2 1.3C6.2 8.8 3 5.8 3.4 2.6z" fill="#2a2d31"/></svg>
        +61 2 5550 1234
      </li>
      <li>
        <svg viewBox="0 0 12 12" aria-hidden="true"><rect width="12" height="12" rx="2" fill="#fff"/><circle cx="6" cy="6" r="3.4" fill="none" stroke="#2a2d31" stroke-width="1.1"/><circle cx="6" cy="6" r="1.3" fill="#2a2d31"/></svg>
        hello@lumorastudio.net.au
      </li>
      <li>
        <svg viewBox="0 0 12 12" aria-hidden="true"><rect width="12" height="12" rx="2" fill="#fff"/><path d="M6 2.2a2.5 2.5 0 0 0-2.5 2.5C3.5 6.6 6 9.8 6 9.8s2.5-3.2 2.5-5.1A2.5 2.5 0 0 0 6 2.2z" fill="#2a2d31"/><circle cx="6" cy="4.7" r="0.9" fill="#fff"/></svg>
        128 Harbour Street, Lindfield, NSW 2070
      </li>
    </ul>

    <div class="web-band">www.lumorastudio.net.au</div>
  </section>

  <section class="card card-back" aria-label="Business card back">
    <div class="back-mark">
      <span class="word-main">lumora</span>
      <span class="word-sub">STUDIO</span>
    </div>
  </section>

</main>
</body>
</html>
```